La Paloma Taberna

We need layouts for the attached 6 pages. The elements that are within the PDF are to be included in the design but their placement, the colors, everything that is there is completely up to your design ability so please get creative.
We like clean, web 2.0 type designs. Here is a restaurant with a nice design:http://tierrasolferino.example/ It does not need to be like this at all, just for a concept of what we like.
The logo on the top left of the site is our logo. I've attached it and a PDF containing the elements of the site here.

```html
<!DOCTYPE html>
<html lang="en">
<head>
<meta charset="utf-8">
<title>La Paloma Taberna — Restaurant &amp; Bar</title>
<link rel="stylesheet" href="https://fonts.googleapis.com/css2?family=Bebas+Neue&family=Caveat:wght@400;500&family=Open+Sans:wght@300;400;600&display=swap">
<style>
  :root{
    --page:#140e03;
    --footer:#0b0802;
    --gold:#e6b93f;
    --gold-light:#f0cd5e;
    --gold-deep:#c99a24;
    --gold-text:#e9b52c;
    --panel:#4a3a15;
    --field:#3a2b06;
    --field-line:#5f4b1a;
    --ink-dark:#2a1d03;
    --text:#f1ece2;
    --promo-yellow:#f9bd0b;
    --promo-grey:#3e3e3e;
    --promo-back:#e9eef5;
  }
  *{margin:0;padding:0;box-sizing:border-box}
  html,body{width:1174px;height:1200px;overflow:hidden;background:var(--page)}
  body{position:relative;font-family:"Open Sans",sans-serif;color:var(--text)}

  .brand{position:absolute;left:117px;top:34px;width:140px;text-align:center}
  .brand-mark{width:42px;height:42px;margin:0 auto 8px;background:var(--gold-deep)}
  .brand-name{font-size:14px;font-weight:400;color:#fff;letter-spacing:.5px;white-space:nowrap}
  .brand-tag{font-size:9px;letter-spacing:1.5px;color:#fff;margin-top:2px;border-top:1px solid #fff;padding-top:2px;display:inline-block}

  .social{position:absolute;top:94px;right:138px;display:flex;gap:5px;list-style:none}
  .social li{width:30px;height:30px;border-radius:50%}
  .social .s1{background:#28b6ea}.social .s2{background:#1c57a8}.social .s3{background:#e0461c}
  .social .s4{background:#2d3d8a}.social .s5{background:#d8141b}

  .nav{position:absolute;left:117px;top:135px;width:940px;height:75px;border-radius:14px 14px 0 0;
    background:linear-gradient(var(--gold-light),var(--gold) 60%,#d8a935);display:flex;align-items:center}
  .nav ul{display:flex;list-style:none;height:100%}
  .nav li{height:100%;display:flex;align-items:center;padding:0 16px;border-right:1px solid #c79d2e;
    box-shadow:1px 0 0 #f3d679;font-family:"Caveat",cursive;font-size:24px;color:var(--ink-dark)}
  .nav li:first-child{padding-left:36px}
  .search{position:absolute;right:13px;top:20px;width:278px;height:40px;background:#3b2a06;border-radius:3px;
    display:flex;align-items:center;justify-content:space-between;padding:0 6px 0 5px;font-size:12px;color:#c6b48a}

  .reserve{position:absolute;left:117px;top:210px;width:276px;height:309px;background:var(--panel);text-align:center}
  .reserve h2{font-family:"Caveat",cursive;font-weight:400;font-size:28px;color:var(--gold-text);margin-top:10px;line-height:1}
  .reserve .powered{font-size:10.5px;font-weight:300;color:var(--gold-text);margin-top:7px}
  .field{position:absolute;left:21px;width:234px;height:42px;background:var(--field);border:1px solid var(--field-line);
    border-radius:3px;display:flex;align-items:center;font-size:13px;font-weight:300;color:#d5bb70;letter-spacing:-.3px}
  .field .ico{width:36px;height:36px;margin:0 5px 0 3px;background:linear-gradient(var(--gold-light),var(--gold-deep));
    border-radius:2px;display:flex;align-items:center;justify-content:center}
  .f1{top:76px}.f2{top:135px}.f3{top:198px}
  .find{position:absolute;left:72px;top:251px;width:136px;height:36px;border-radius:3px;
    background:linear-gradient(#f8da6c,#e3b23a);color:var(--ink-dark);font-weight:600;font-size:13px;letter-spacing:-.3px;
    display:flex;align-items:center;justify-content:center}

  .hero{position:absolute;left:393px;top:210px;width:664px;height:309px;
    background:radial-gradient(ellipse at 55% 55%,#c9a66a 0%,#8a5a24 30%,#5a3b1a 55%,#cfcac2 100%)}
  .dots{position:absolute;left:296px;bottom:9px;display:flex;gap:6px;list-style:none}
  .dots li{width:15px;height:15px;border-radius:50%;background:#fff}
  .dots li:first-child{background:var(--gold-deep)}

  .promo{position:absolute;left:117px;top:539px;width:276px;height:480px;background:var(--promo-back)}
  .promo-card{position:absolute;left:22px;top:0;width:234px;height:273px;background:var(--promo-yellow)}
  .promo-tab{position:absolute;left:55px;top:0;width:122px;height:52px;background:var(--promo-grey)}
  .promo-copy{position:absolute;left:55px;top:44px;width:124px;overflow:hidden;font-family:"Bebas Neue",sans-serif;
    font-weight:400;text-transform:uppercase;color:var(--ink-dark);line-height:.9;white-space:nowrap}
  .promo-copy .great{font-size:60px;color:#fff}
  .promo-copy .deals{font-size:44px}
  .promo-copy .small{font-size:37px}
  .promo-copy .last{font-size:47px}
  .buy{position:absolute;left:55px;top:218px;width:124px;height:37px;background:var(--ink-dark);color:#fff;
    font-family:"Bebas Neue",sans-serif;font-size:30px;display:flex;align-items:center;justify-content:center;padding-top:3px}
  .promo-photo{position:absolute;left:0;top:273px;width:276px;height:207px;
    background:radial-gradient(ellipse at 50% 45%,#b5714a 0%,#c8a17a 35%,#f3f3f4 62%,#e5e9ee 100%)}

  .welcome{position:absolute;left:419px;top:554px;width:640px}
  .welcome h1{font-family:"Caveat",cursive;font-weight:400;font-size:45px;color:var(--gold-text);line-height:1}
  .welcome h3{font-family:"Caveat",cursive;font-weight:400;font-size:32px;color:#fff;line-height:1;margin-top:6px}
  .welcome p{margin-top:26px;font-size:14px;font-weight:300;letter-spacing:-.5px;word-spacing:-.5px;line-height:23.5px;color:var(--text)}

  .footer{position:absolute;left:0;top:1065px;width:1174px;height:135px;background:var(--footer);text-align:center}
  .footer ul{list-style:none;display:flex;justify-content:center;margin-top:31px;font-family:"Caveat",cursive;font-size:21px}
  .footer li{padding:0 11px;border-left:1px solid #fff;line-height:22px}
  .footer li:first-child{border-left:0}
  .footer .copy{font-family:"Caveat",cursive;font-size:21px;margin-top:18px}
  .footer .code{position:absolute;right:14px;top:71px;font-size:13px;color:#8a8a8a}
</style>
</head>
<body>
  <header>
    <div class="brand">
      <div class="brand-mark"></div>
      <div class="brand-name">La Paloma Taberna</div>
      <div class="brand-tag">Restaurant &amp; Bar</div>
    </div>
    <ul class="social" aria-label="Social links">
      <li class="s1"></li><li class="s2"></li><li class="s3"></li><li class="s4"></li><li class="s5"></li>
    </ul>
    <nav class="nav">
      <ul>
        <li>Home</li><li>Menu</li><li>Contact</li><li>Calendar</li><li>Press</li><li>Gallery</li>
      </ul>
      <div class="search">
        <span>Search</span>
        <svg width="24" height="22" viewBox="0 0 24 22"><circle cx="8" cy="8" r="6" fill="none" stroke="#fff" stroke-width="2.5"/><line x1="12.5" y1="12.5" x2="21" y2="19.5" stroke="#fff" stroke-width="4" stroke-linecap="round"/></svg>
      </div>
    </nav>
  </header>

  <section class="reserve">
    <h2>Make A Reservation</h2>
    <div class="powered">POWERED BY TABLENEST</div>
    <div class="field f1"><span class="ico"><svg width="20" height="20" viewBox="0 0 20 20"><rect x="1" y="3" width="18" height="16" fill="#5a4204"/><rect x="4" y="0" width="3" height="5" fill="#5a4204"/><rect x="13" y="0" width="3" height="5" fill="#5a4204"/><g fill="#e6b93f"><rect x="4" y="9" width="3" height="2"/><rect x="9" y="9" width="3" height="2"/><rect x="14" y="9" width="2" height="2"/><rect x="4" y="13" width="3" height="2"/><rect x="9" y="13" width="3" height="2"/><rect x="14" y="13" width="2" height="2"/></g></svg></span>19-6-2014</div>
    <div class="field f2"><span class="ico"><svg width="20" height="20" viewBox="0 0 20 20"><circle cx="10" cy="10" r="8" fill="none" stroke="#5a4204" stroke-width="2"/><path d="M10 5v5h4" fill="none" stroke="#5a4204" stroke-width="2"/></svg></span>7.00 PM</div>
    <div class="field f3"><span class="ico"><svg width="20" height="20" viewBox="0 0 20 20"><circle cx="10" cy="6" r="4.5" fill="#5a4204"/><path d="M2 19c0-6 4-8 8-8s8 2 8 8z" fill="#5a4204"/></svg></span>2 People</div>
    <div class="find">FIND A TABLE</div>
  </section>

  <section class="hero" role="img" aria-label="Plated seared fish fillet with grilled greens">
    <ul class="dots"><li></li><li></li><li></li><li></li></ul>
  </section>

  <aside class="promo">
    <div class="promo-card">
      <div class="promo-tab"></div>
      <div class="promo-copy">
        <div class="great">Great</div>
        <div class="deals">Deals in</div>
        <div class="small">La Paloma</div>
        <div class="last">Taberna</div>
      </div>
      <div class="buy">BUY NOW</div>
    </div>
    <div class="promo-photo" role="img" aria-label="Grilled chicken salad in a white bowl"></div>
  </aside>

  <main class="welcome">
    <h1>Welcome to La Paloma Taberna</h1>
    <h3>Restaurant &amp; Bar</h3>
    <p>La Paloma Taberna, a new upscale 181-seat restaurant and lounge close to the Las Vegas Strip, will open to the public on Friday, June 20 and the grand opening is slated for July 24. The concept will present authentic Mexican cuisine representing the regions of Mexico and its vast culinary traditions. We believe strongly that sustainably-raised products and offering superior quality in our incredibly flavorful food keeps the high standards of our guests in mind. All of our beef, chicken, pork, shrimp and fish originates from carefully-selected in the US and are free of antibiotics, pesticides and steroids. The Bar offers delicious white, red and sparkling Sangrias house made with fresh fruits, assorted domestic, import beers and specialty craft beers including Harrow Pure Brewed Organic Lager, Lantern Night IPA, wines, champagne, bottle service and more than 100 tequilas such as Sierra Alta 'Reserva' 11-Year aged and Cielo Fino Ultra. The decor is sophisticated with its rich brown woods, hand-woven deep red wall coverings, wrought-iron Mexican light fixtures adding a soft lighting ambiance, custom built-in lighted birch wood boxes showcasing premium Tequilas, several antique mirrors, and two beautifully-aged antique Mexican oak and copper doors hung near the bar. The private dining room accommodates up to 40 persons and is available for catered banquets, parties, meetings and buyouts</p>
  </main>

  <footer class="footer">
    <ul><li>Home</li><li>Menu</li><li>Contact</li><li>Calendar</li><li>Press</li><li>Gallery</li></ul>
    <div class="copy">© 2014 La Paloma Taberna ,All Rights reserved.</div>
    <div class="code">C5</div>
  </footer>
</body>
</html>
```